BRAMWELL Sofa Shop - Hipster Hero Header Design

I want to use the 'Meridale' theme on Storvik

https://meridale-theme-basic.storvikshop.example/
https://themes.storvikshop.example/themes/meridale/styles/plenwise/preview

The main, PRIMARY thing that I need designed is the top hero header to be customized to my shop. Please use the attached examples as a reference. I welcome creativity. I do like the hipster vibe. I'd like a sofa/Living Room theme.

****To be clear...I want a hipster header designed...I love the creative fonts on a filtered relevant photo*** I have placed attachments. Hipster fonts or a Badge, or some combo. If you need guidance please look at examples.

Words on design should be:

BRAMWELL SOFA SHOP.

(I will separately handle the functionality of the site.)
Thanks.
Updates

Please check my brief as I have streamlined my desires. I simply want a hero header designed and 3 buttons designed. Examples of hero headers are attached. Thanks. Added Saturday, September 26, 2015

Target Market(s)

Sofa Shoppers

Industry/Entity Type

Furniture Store

Number of Pages Required

1 page

Requirements
Nice to have
• Bramwell Sofa Shop
• https://meridale-theme-basic.storvikshop.example/

```html
<!DOCTYPE html>
<html lang="en">
<head>
<meta charset="utf-8">
<title>Bramwell Sofa Shop</title>
<link rel="stylesheet" href="https://fonts.googleapis.com/css2?family=Open+Sans:wght@400;600;700&display=swap">
<style>
:root{
  --green:#4fae92;
  --ink:#333333;
  --muted:#777777;
  --white:#ffffff;
  --footer:#262626;
  --card-bar:#9a9a9a;
  --chip:#3a3a3a;
}
*{box-sizing:border-box;margin:0;padding:0}
html,body{width:857px;height:1200px;overflow:hidden;background:var(--white)}
body{font-family:'Open Sans',Arial,sans-serif;color:var(--ink);position:relative}

/* Hero */
.hero{position:absolute;left:0;top:0;width:857px;height:330px;
  background:radial-gradient(ellipse at 35% 70%,#7a2a24 0%,#4a2320 35%,#2b2220 70%,#1d1b1a 100%)}
.hero-title{position:absolute;left:0;right:0;top:118px;text-align:center;color:var(--white)}
.hero-title .kicker{font-size:12px;letter-spacing:.5px;margin-bottom:8px}
.hero-title .name{display:inline-block;border:2px solid var(--white);padding:10px 36px;font-size:26px;font-weight:600;letter-spacing:.5px}
.hero-dots{position:absolute;top:296px;left:0;right:0;text-align:center}
.hero-dots span{display:inline-block;width:8px;height:8px;border-radius:50%;background:#bbb;margin:0 3px}
.hero-dots span.on{background:var(--white)}
.nav{position:absolute;right:30px;top:22px;width:90px;text-align:center}
.nav .icons{display:flex;justify-content:center;gap:12px;margin-bottom:10px}
.nav ul{list-style:none}
.nav li{color:var(--white);font-size:18px;line-height:22px}
.nav li.active{color:var(--green)}

/* Section headings */
.section-head{display:flex;align-items:center;gap:16px;justify-content:center;font-size:17px;font-weight:700;letter-spacing:.5px}
.section-head::before,.section-head::after{content:"";width:290px;height:1px;background:var(--ink)}
.btn-outline{display:inline-block;border:1px solid var(--ink);font-size:9px;font-weight:600;padding:6px 14px;letter-spacing:.5px}

/* About */
.about{position:absolute;left:0;top:345px;width:857px;height:140px;text-align:center}
.about p{width:600px;margin:14px auto 14px;font-size:9.5px;line-height:14px;color:var(--muted)}

/* Feature band */
.features{position:absolute;left:0;top:485px;width:857px;height:275px;
  background:linear-gradient(90deg,#2c2c2c 0%,#3d3632 45%,#2a2a2a 100%)}
.feature{position:absolute;top:55px;width:160px;text-align:center;color:var(--white)}
.feature .photo{width:100px;height:100px;border-radius:50%;margin:0 auto 8px;border:3px solid var(--white)}
.feature h3{color:var(--green);font-size:12px;font-weight:600}
.feature p{font-size:8.5px;line-height:12px;margin:3px auto 8px;width:150px;color:#e6e6e6}
.btn-green{display:inline-block;background:var(--green);color:var(--white);font-size:9px;font-weight:600;padding:4px 10px}

/* Products */
.products{position:absolute;left:0;top:785px;width:857px;height:260px;text-align:center}
.product-grid{position:absolute;left:108px;top:40px;display:flex;gap:12px}
.product{width:158px;border:1px solid #ddd}
.product .photo{height:112px;background:#fff;position:relative}
.product .photo i{position:absolute;left:18px;right:18px;top:26px;bottom:20px;border-radius:8px;display:block}
.product .bar{background:var(--card-bar);height:28px;display:flex;align-items:center;justify-content:space-between;padding:0 6px;color:var(--white);font-size:8px;text-align:left;line-height:10px}
.product .buy{background:var(--green);padding:4px 9px;font-weight:700}
.products .browse{position:absolute;left:0;right:0;top:226px}

/* Footer */
.footer{position:absolute;left:0;top:1052px;width:857px;height:128px;background:var(--footer);color:var(--white)}
.footer .col{position:absolute;top:22px;font-size:9px;line-height:13px;color:#cfcfcf}
.footer h4{color:var(--white);font-size:11px;font-weight:700;margin-bottom:6px}
.signup{display:flex;margin-top:4px}
.signup .field{width:120px;height:18px;background:var(--white);color:#999;font-size:8px;padding:3px 6px}
.signup .go{height:18px;background:#111;color:var(--white);font-size:8px;padding:3px 8px;border:1px solid #555}
.pay{display:flex;gap:6px;margin-top:6px;align-items:center}
.pay span{font-size:9px;font-weight:600;color:var(--white);background:var(--chip);padding:4px 6px}
.copy{position:absolute;left:0;top:1180px;width:857px;height:20px;background:var(--green);color:var(--white);font-size:8px;display:flex;align-items:center;justify-content:center}
.copy .social{position:absolute;right:20px;top:4px;display:flex;gap:5px}
.copy .social i{width:12px;height:12px;border-radius:50%;background:var(--white);display:block;opacity:.85}
</style>
</head>
<body>

<header class="hero" role="img" aria-label="Dim living room with a red sofa as hero background">
  <nav class="nav">
    <div class="icons">
      <svg width="14" height="14" viewBox="0 0 14 14"><circle cx="6" cy="6" r="4.5" fill="none" stroke="#fff" stroke-width="2"/><line x1="9.5" y1="9.5" x2="13" y2="13" stroke="#fff" stroke-width="2"/></svg>
      <svg width="13" height="13" viewBox="0 0 13 13"><path d="M2 2L11 11M11 2L2 11" stroke="#fff" stroke-width="2.5"/></svg>
    </div>
    <ul>
      <li class="active">Home</li><li>Menu</li><li>Blog</li><li>Gallery</li><li>Shop</li><li>Sign In</li><li>Close</li>
    </ul>
  </nav>
  <div class="hero-title">
    <div class="kicker">Lorem ipsum</div>
    <div class="name">BRAMWELL Sofa Shop</div>
  </div>
  <div class="hero-dots"><span class="on"></span><span class="on"></span><span></span></div>
</header>

<section class="about">
  <h2 class="section-head">ABOUT US</h2>
  <p>Vivamus sed erat sagittis magna consequat sagittis. Nulla faucibus enim a magna id tincidunt accumsan. Curabitur laoreet dapibus nisi sem lorem fermentum molestie. Cras posuere orci leo lobortis fermentum. Phasellus aliquam nisl et dolor pharetra, ligula magna fermentum justo.</p>
  <span class="btn-outline">READ MORE</span>
</section>

<section class="features" role="img" aria-label="Couple relaxing on a sofa, darkened background photo">
  <div class="feature" style="left:110px">
    <div class="photo" role="img" aria-label="Red armchair" style="background:radial-gradient(circle,#b84a3a,#f2ece6 70%)"></div>
    <h3>Lorem ipsum dolor sit</h3>
    <p>Consectetur adipiscing elit, pellentesque imperdiet lorem vel in pulvinar.</p>
    <span class="btn-green">Read more</span>
  </div>
  <div class="feature" style="left:348px">
    <div class="photo" role="img" aria-label="Tan leather sofa" style="background:radial-gradient(circle,#b48a5c,#f4efe8 70%)"></div>
    <h3>Lorem ipsum dolor sit</h3>
    <p>Consectetur adipiscing elit, pellentesque imperdiet lorem vel in pulvinar.</p>
    <span class="btn-green">Read more</span>
  </div>
  <div class="feature" style="left:586px">
    <div class="photo" role="img" aria-label="Red fabric sofa" style="background:radial-gradient(circle,#a3263a,#f2ece8 70%)"></div>
    <h3>Lorem ipsum dolor sit</h3>
    <p>Consectetur adipiscing elit, pellentesque imperdiet lorem vel in pulvinar.</p>
    <span class="btn-green">Read more</span>
  </div>
</section>

<section class="products">
  <h2 class="section-head">FEATURED PRODUCTS</h2>
  <div class="product-grid">
    <div class="product"><div class="photo"><i role="img" aria-label="Purple armchair" style="background:#6c4a8a"></i></div><div class="bar"><span>Lorem ipsum<br>$199.00</span><span class="buy">BUY</span></div></div>
    <div class="product"><div class="photo"><i role="img" aria-label="Red sofa" style="background:#c8402e"></i></div><div class="bar"><span>Lorem ipsum<br>$199.00</span><span class="buy">BUY</span></div></div>
    <div class="product"><div class="photo"><i role="img" aria-label="Dark green chesterfield sofa" style="background:#1f4034"></i></div><div class="bar"><span>Lorem ipsum<br>$199.00</span><span class="buy">BUY</span></div></div>
    <div class="product"><div class="photo"><i role="img" aria-label="Black leather sofa" style="background:#2a2a2a"></i></div><div class="bar"><span>Lorem ipsum<br>$199.00</span><span class="buy">BUY</span></div></div>
  </div>
  <div class="browse"><span class="btn-outline">BROWSE MORE PRODUCTS</span></div>
</section>

<footer class="footer">
  <div class="col" style="left:110px"><h4>Quick Links</h4>Collections<br>Lookbook<br>All Categories<br>Shop By Brand</div>
  <div class="col" style="left:235px"><h4>FAQ'S</h4>Lorem ipsum<br>Dolor sit amet<br>Consectetur<br>Adipiscing elit</div>
  <div class="col" style="left:335px"><h4>Sign up for deals</h4>
    <div class="signup"><span class="field">E-mail Address</span><span class="go">Sign up</span></div>
  </div>
  <div class="col" style="left:570px"><h4>Payment Method</h4>
    <div class="pay"><span>Corvan</span><span>Ombrel</span><span>Tellix</span><span>Quillo</span></div>
  </div>
</footer>
<div class="copy">Copyright &copy; 2015 Bramwell Sofa Shop. All rights reserved.
  <div class="social"><i></i><i></i><i></i><i></i></div>
</div>

</body>
</html>
```